Various Designs

We need various designs for our new hand disinfectant dispensers that feature three extra-large windows that allow users to customize the appearance simply by changing the graphics.
Each dispenser has one window at the front and one on each side. The front window can have two different sizes. Please refer to attached zip file named Dispenser_Design_Templates.
The designs should be fresh and of high quality. Please don't just place a photo and spam me.
The design should also contain our logo (Brunvale Helvetia - is included in the template).
The design should further be professional enough for a medical and public setting. The dispensers will be used in hospitals, medical facilities, old pension homes, schools, restaurants, kitchens, public places etc.
We value creativity a lot!
It would be great if the dispenser features a slogan such as "Hand Hygiene Saves Lives". I have added a number of slogans at the end of this description.
Do not use dark colors such as brown. These colors do not stand for hygiene. You can use black but only in conjunction with a bright color.
The following files contain designs that I like:
- 01w
- velmixdecor
- worldwide
- IMG_0137
Slogans:
- Hand Hygiene Saves Lives
- Did you wash your hands?
- Did you disinfect your hands?
- Protect Yourself and Your Patients
- Healthy Hands Start Here
- Hand Hygiene We Love... We Care... We Share...
- Clean hands prevent germs from spreading.
- Practice Good Hand Hygiene
- Save Lives: Clean Your Hands
- Save Lives: Disinfect Your Hands
- Washing Hands Saves Lives
- Wash Your Hands Please
- Be aware…..!!!!! Wash with care…..!!!!!
- Hand Hygiene Station
- Hand Hygiene Share your care, not your germs
- Good Hand Hygiene It's Critical Sanitize Wash Moisturize
- Disinfect (image of a hand)
- Clean (image of a hand)
- No Water? No Problem. Waterless Hand Rub. Keep it Handy.
- Wash your hands! If not for yourself, then do it for them.
- Practice good hygiene - it-s contagious!
- Be aware, wash with care!
- Filthy fingers forecast sickness and sadness.
- Hand Hygiene The power is in your hands
- Bury the germ, Wash your hands
- Sanitize your hands and support our clean hands initiative
- Sanitize your hands. Together we can make a difference.
- You are grand if you wash your hand.
- Holding hands feels better when they’re clean.
- Be wise wash hands often.
- Wash those germs away!!!
- Your Hands Can Be Dangerous. Disinfect them to keep germs away.
- Ten out of ten patients prefer care from clean hands.
- Safety first, disinfect and protect
- It’s universal- handwashing every patient every time!
- Infection control is in your hands.
- Make your intention prevention. Wash your hands

```html
<!DOCTYPE html>
<html lang="en">
<head>
<meta charset="utf-8">
<title>Brunvale Helvetia – Dispenser Window Graphics</title>
<link href="https://fonts.googleapis.com/css2?family=Ubuntu:wght@500&family=Baloo+2:wght@700&display=swap" rel="stylesheet">
<style>
  :root {
    --page: #ffffff;
    --cream: #fbf7ea;
    --petal: #f3ecd8;
    --petal-shade: #e9e2cf;
    --pollen: rgba(246, 222, 40, .85);
    --pollen-soft: rgba(248, 230, 90, .6);
    --anther: rgba(236, 160, 30, .85);
    --blush: rgba(214, 40, 120, .75);
    --brand: #8c2a48;
    --slogan: #5b95d6;
    --cut-line: #e0232e;
    --safe-line: #6cbf5c;
    --bleed-line: #f2d51e;
  }
  * { margin: 0; padding: 0; box-sizing: border-box; }
  html, body { width: 1200px; height: 1000px; overflow: hidden; background: var(--page); }
  .canvas { position: relative; width: 1200px; height: 1000px; }
  .window { position: absolute; top: 60px; height: 880px; overflow: hidden; background: var(--cream); }
  .window--left  { left: 0;   width: 297px; }
  .window--front { left: 392px; width: 422px; }
  .window--right { left: 903px; width: 297px; }
  .flower-photo { position: absolute; inset: 0; }

  .window--left .flower-photo {
    background:
      radial-gradient(ellipse 40px 120px at 195px 255px, var(--anther), transparent 85%),
      radial-gradient(ellipse 85px 42px at 145px 455px, var(--anther), transparent 85%),
      radial-gradient(ellipse 150px 110px at 220px 520px, var(--pollen), transparent 80%),
      radial-gradient(ellipse 300px 220px at 170px 470px, var(--pollen-soft), transparent 80%),
      radial-gradient(ellipse 120px 50px at 60px 330px, rgba(214,40,120,.25), transparent 80%),
      radial-gradient(ellipse 260px 150px at 120px 780px, var(--petal-shade), transparent 80%),
      linear-gradient(180deg, var(--cream) 0%, #f7f0dc 40%, var(--petal) 70%, #f1eadb 100%);
  }
  .window--front .flower-photo {
    background:
      radial-gradient(ellipse 60px 300px at 65px 290px, var(--pollen), transparent 85%),
      radial-gradient(ellipse 40px 110px at 85px 360px, var(--anther), transparent 85%),
      radial-gradient(ellipse 40px 110px at 175px 230px, var(--anther), transparent 85%),
      radial-gradient(ellipse 90px 48px at 285px 355px, var(--anther), transparent 85%),
      radial-gradient(ellipse 110px 50px at 350px 350px, var(--blush), transparent 80%),
      radial-gradient(ellipse 230px 200px at 110px 560px, var(--pollen), transparent 80%),
      radial-gradient(ellipse 380px 260px at 200px 560px, var(--pollen-soft), transparent 80%),
      radial-gradient(ellipse 260px 180px at 300px 780px, var(--petal-shade), transparent 80%),
      linear-gradient(180deg, var(--cream) 0%, #f7f0dc 45%, var(--petal) 75%, #f1eadb 100%);
  }
  .window--right .flower-photo {
    background:
      radial-gradient(ellipse 35px 110px at 100px 235px, var(--anther), transparent 85%),
      radial-gradient(ellipse 95px 45px at 175px 365px, var(--anther), transparent 85%),
      radial-gradient(ellipse 110px 50px at 260px 345px, var(--blush), transparent 80%),
      radial-gradient(ellipse 170px 160px at 80px 560px, var(--pollen), transparent 80%),
      radial-gradient(ellipse 300px 240px at 110px 540px, var(--pollen-soft), transparent 80%),
      radial-gradient(ellipse 260px 160px at 170px 780px, var(--petal-shade), transparent 80%),
      linear-gradient(180deg, var(--cream) 0%, #f7f0dc 40%, var(--petal) 70%, #f1eadb 100%);
  }

  .template-guides { position: absolute; left: 0; top: 0; width: 1200px; height: 1000px; }
  .template-guides path, .template-guides circle { fill: none; stroke-width: 1.2; }
  .cut { stroke: var(--cut-line); }
  .safe { stroke: var(--safe-line); }
  .bleed { stroke: var(--bleed-line); }

  .brand-name {
    position: absolute; top: 199px; left: 392px; width: 422px; text-align: center;
    font-family: "Ubuntu", sans-serif; font-weight: 500; font-size: 27px; line-height: 32px;
    color: var(--brand); letter-spacing: .5px;
  }
  .slogan {
    position: absolute; top: 523px; left: 392px; width: 422px; text-align: center;
    font-family: "Baloo 2", sans-serif; font-weight: 700; font-size: 21px; line-height: 25.5px;
    color: var(--slogan);
  }
</style>
</head>
<body>
<main class="canvas">
  <section class="window window--left">
    <div class="flower-photo" role="img" aria-label="Soft close-up photograph of a white lily with golden stamens"></div>
  </section>
  <section class="window window--front">
    <div class="flower-photo" role="img" aria-label="Soft close-up photograph of a white lily with yellow pistil, golden stamens and a pink petal edge"></div>
  </section>
  <section class="window window--right">
    <div class="flower-photo" role="img" aria-label="Soft close-up photograph of a white lily with golden stamens and a pink petal edge"></div>
  </section>

  <svg class="template-guides" viewBox="0 0 1200 1000" aria-hidden="true">
    <g class="side-guide">
      <path class="cut" d="M20 72 L256 76 Q270 78 271 92 L292 912 L75 912 L62 700 Q55 620 20 560 Z"/>
      <path class="safe" d="M22 90 L240 92 Q256 94 257 110 L276 888 L76 888 L64 700 Q58 625 22 568 Z"/>
      <path class="bleed" d="M22 92 L228 94 Q242 96 243 112 L262 886 L80 886 L68 700 Q62 625 24 570 Z"/>
      <circle class="cut" cx="44" cy="80" r="5"/>
      <circle class="cut" cx="252" cy="86" r="5"/>
      <circle class="cut" cx="99" cy="901" r="5"/>
      <circle class="cut" cx="266" cy="892" r="5"/>
    </g>
    <g class="side-guide" transform="translate(1200 0) scale(-1 1)">
      <path class="cut" d="M20 72 L256 76 Q270 78 271 92 L292 912 L75 912 L62 700 Q55 620 20 560 Z"/>
      <path class="safe" d="M22 90 L240 92 Q256 94 257 110 L276 888 L76 888 L64 700 Q58 625 22 568 Z"/>
      <path class="bleed" d="M22 92 L228 94 Q242 96 243 112 L262 886 L80 886 L68 700 Q62 625 24 570 Z"/>
      <circle class="cut" cx="44" cy="80" r="5"/>
      <circle class="cut" cx="252" cy="86" r="5"/>
      <circle class="cut" cx="99" cy="901" r="5"/>
      <circle class="cut" cx="266" cy="892" r="5"/>
    </g>
    <g class="front-guide">
      <path class="cut" d="M408 70 L797 70 L746 893 L460 893 Z"/>
      <path class="safe" d="M480 88 Q600 82 720 88 Q768 92 768 140 L722 840 Q718 880 680 882 L528 882 Q490 880 486 840 L440 140 Q440 92 480 88 Z"/>
      <path class="bleed" d="M484 92 Q600 86 716 92 Q760 96 760 142 L716 838 Q712 876 676 878 L532 878 Q496 876 492 838 L448 142 Q448 96 484 92 Z"/>
      <circle class="cut" cx="433" cy="99" r="5"/>
      <circle class="cut" cx="771" cy="99" r="5"/>
      <circle class="cut" cx="481" cy="867" r="5"/>
      <circle class="cut" cx="724" cy="867" r="5"/>
    </g>
  </svg>

  <div class="brand-name">Brunvale Helvetia</div>
  <p class="slogan">Be<br>Hygiene Serene.<br>Keep Your Hands Clean.</p>
</main>
</body>
</html>
```